Modern Website Design for PollBeacon – CX & Loyalty SaaS Platform

We need a modern, professional, and responsive website design for our B2B SaaS platform, PollBeacon. We help companies collect real-time customer feedback, analyze insights, and improve loyalty — combining a powerful CX platform with expert consulting services. The website should clearly communicate who we are and what we offer within the first impression. It should balance data-driven visuals such as dashboards, analytics, and charts with a human, approachable feel. The design must include at least six key pages: Homepage, Product/Services, About, Blog/Resources, Contact/Demo, and Pricing. It should be conversion-focused with clear calls-to-action that encourage visitors to request a demo or contact us. The site must be fully responsive across desktop, tablet, and mobile. It should support multiple languages, starting with English and Danish. Most importantly, the delivery must be a final WordPress website, ready to go live, not just design files.

Target Market(s)

Our target market is medium-to-large B2B organizations. The primary audience includes CX leaders, executives, and managers in customer success and service who want to measure loyalty, understand customer insights, and improve retention.

Industry/Entity Type

Technology / SaaS / Customer Experience

Coding

Coded - Design and coding required

Number of Pages Required

5+ page

Font styles to use
Sans Serif

Requirements
Must have
• The project must deliver a final WordPress website that is fully responsive across all devices. The design should be clean, modern, and SaaS-inspired, with clear calls-to-action on every page. It must also support English and Danish, with a visible language toggle. The site should include visuals of dashboards and analytics that reflect data-driven insights. It must feature sections for case studies or testimonials to build trust. The copywriting should be SEO-friendly, and the design should include smooth animations or hover effects that add polish without making the website feel heavy.
Should not have
• Cluttered layouts, or generic stock photos such as handshakes

```html
<!DOCTYPE html>
<html lang="en">
<head>
<meta charset="utf-8">
<title>PollBeacon – Website Pages</title>
<link href="https://fonts.googleapis.com/css2?family=Inter:wght@400;500;600;700&display=swap" rel="stylesheet">
<style>
:root{
  --bg:#a9aaab;
  --ink:#111827;
  --muted:#6b7280;
  --blue:#2563eb;
  --blue-dk:#1d4ed8;
  --teal:#0f9b8e;
  --line:#e5e7eb;
  --soft:#f5f7fa;
  --navy:#1f2736;
  --hero1:#e7ebf1;
  --hero2:#d3d9e3;
  --green:#16a34a;
}
*{box-sizing:border-box;margin:0;padding:0}
html,body{width:1200px;height:604px;overflow:hidden;background:var(--bg)}
body{font-family:'Inter',Arial,sans-serif;color:var(--ink)}
.board{position:absolute;left:0;top:0;width:2576px;height:1297px;transform:scale(.46584);transform-origin:0 0}
.page{position:absolute;top:24px;width:396px;background:#fff;overflow:hidden;display:flex;flex-direction:column}
.p1{left:62px;height:771px}.p2{left:475px;height:1211px}.p3{left:889px;height:985px}
.p4{left:1302px;height:1203px}.p5{left:1716px;height:1042px}.p6{left:2130px;height:1028px}

/* header */
.site-head{height:26px;flex:none;display:flex;align-items:center;padding:0 65px;background:#fff;font-size:3.6px}
.logo{display:flex;align-items:center;gap:2px;font-weight:700;font-size:5.2px;color:var(--ink)}
.logo-dot{width:6px;height:6px;border-radius:50%;background:var(--blue)}
.site-head nav{display:flex;gap:6px;margin-left:auto;color:#374151}
.site-head nav .on{color:var(--blue)}
.lang{margin-left:8px;color:#374151}
.btn{display:inline-block;background:var(--blue);color:#fff;font-size:3.4px;padding:2.4px 5px;border-radius:1.2px;font-weight:500}
.btn-o{display:inline-block;border:.5px solid var(--blue);color:var(--blue);background:#fff;font-size:3.4px;padding:2px 5px;border-radius:1.2px}
.site-head .btn{margin-left:6px}

/* hero */
.hero{position:relative;height:188px;flex:none;overflow:hidden}
.hero-photo{position:absolute;inset:0;background:linear-gradient(100deg,var(--hero1) 0%,#dde2ea 55%,var(--hero2) 100%)}
.hero-text{position:absolute;left:65px;width:128px}
.hero h1{font-size:13.5px;line-height:1.02;font-weight:700;letter-spacing:-.2px}
.hero h1 em{font-style:normal;color:var(--blue)}
.hero p{font-size:3.3px;line-height:1.45;color:#4b5563;margin-top:6px}
.hero .actions{margin-top:7px;display:flex;gap:4px}
.hero-stats{display:flex;gap:9px;margin-top:14px}
.hero-stats b{display:block;font-size:7px;color:var(--blue)}
.hero-stats span{font-size:2.6px;color:var(--muted)}
.toggle{display:flex;gap:8px;align-items:center;font-size:3px;margin-top:8px}
.toggle i{width:9px;height:4.5px;border-radius:3px;background:#fff;border:.4px solid #cbd5e1}
.toggle em{font-style:normal;color:var(--green)}

.dash{position:absolute;left:208px;width:125px;background:#fff;border-radius:3px;box-shadow:0 3px 10px rgba(15,23,42,.12);padding:6px}
.dash-top{display:flex;justify-content:space-between;font-size:3.2px;font-weight:600}
.dash-top span{color:var(--green);font-weight:500;font-size:2.6px}
.dash-sub{display:flex;justify-content:space-between;font-size:2.6px;margin-top:7px;font-weight:600}
.dash-sub span{color:var(--muted);font-weight:400}
.bars{display:flex;align-items:flex-end;gap:4px;height:22px;margin-top:6px}
.bars i{flex:1;background:linear-gradient(180deg,var(--blue),var(--teal));border-radius:.6px}
.dash-stats{display:flex;justify-content:space-around;margin-top:8px;text-align:center}
.dash-stats b{display:block;font-size:4.6px;color:var(--blue)}
.dash-stats span{font-size:2.2px;color:var(--muted)}
.float{position:absolute;background:#fff;border-radius:2px;box-shadow:0 2px 6px rgba(15,23,42,.12);padding:3px 4px;display:flex;gap:3px;align-items:center;font-size:2.4px;color:var(--muted)}
.float b{display:block;font-size:4px;color:var(--ink)}

/* sections */
.sec{flex:none;padding:0 65px;text-align:center;position:relative}
.soft{background:var(--soft)}
.sec-title{font-size:8.2px;font-weight:600;padding-top:22px;line-height:1.2}
.sec-sub{font-size:3.4px;color:var(--muted);width:135px;margin:3px auto 0;line-height:1.5}
.grid{display:grid;gap:6px;margin-top:16px;text-align:left}
.g2{grid-template-columns:repeat(2,1fr)}.g3{grid-template-columns:repeat(3,1fr)}.g4{grid-template-columns:repeat(4,1fr)}
.card{background:#fff;border:.5px solid var(--line);border-radius:2px;padding:7px 6px;box-shadow:0 1px 3px rgba(15,23,42,.05)}
.card h4{font-size:3.8px;font-weight:600;margin-top:5px;line-height:1.25}
.card p{font-size:2.8px;color:var(--muted);line-height:1.5;margin-top:3px}
.center{text-align:center}
.center .ico{margin:0 auto}
.ico{display:block;width:8px;height:8px;border-radius:1.6px;background:var(--blue);position:relative}
.ico::after{content:"";position:absolute;left:2.5px;top:2.5px;width:3px;height:3px;border:.6px solid #fff;border-radius:.6px}
.ico.round{border-radius:50%}
.ico.round::after{border-radius:50%}
.ticks{list-style:none;margin-top:4px}
.ticks li{font-size:2.6px;color:#4b5563;line-height:1.9;padding-left:4px;position:relative}
.ticks li::before{content:"";position:absolute;left:0;top:1.5px;width:1.6px;height:.9px;border-left:.5px solid var(--green);border-bottom:.5px solid var(--green);transform:rotate(-45deg)}
.tag{display:inline-block;font-size:2.2px;background:var(--blue);color:#fff;padding:.6px 2px;border-radius:1px}
.meta{font-size:2.3px;color:var(--muted);margin-top:4px}
.link{font-size:2.6px;color:var(--blue);margin-top:3px}

/* testimonials */
.quote{font-style:italic}
.person{display:flex;align-items:center;gap:3px;margin-top:6px}
.avatar{width:7px;height:7px;border-radius:50%;background:linear-gradient(135deg,#d6c3ad,#8b7766);flex:none}
.person b{display:block;font-size:2.6px}
.person span{font-size:2.2px;color:var(--muted)}

/* cta + footer */
.cta{flex:none;background:linear-gradient(100deg,var(--blue) 0%,#1f7fb8 50%,var(--teal) 100%);color:#fff;text-align:center;padding:0 65px}
.cta h3{font-size:7.5px;font-weight:600;padding-top:22px}
.cta p{font-size:3.2px;opacity:.9;margin-top:3px}
.cta .actions{display:flex;gap:4px;justify-content:center;margin-top:8px}
.cta .btn{background:#1d4ed8}
.cta .btn-o{background:transparent;border-color:#fff;color:#fff}
.subscribe{display:flex;justify-content:center;gap:3px;margin-top:7px}
.subscribe i{width:60px;height:6px;background:#fff;border-radius:1px;font-style:normal;font-size:2.4px;color:var(--muted);padding:1.5px 2px}
.foot{flex:none;background:var(--navy);color:#cbd5e1;padding:18px 65px 0}
.foot-row{display:flex;gap:0}
.foot-brand{width:150px}
.foot-brand .logo{color:#fff}
.foot-brand p{font-size:2.8px;line-height:1.5;margin-top:8px;width:80px}
.foot-col{width:40px;font-size:2.5px;line-height:1.9}
.foot-col b{color:#fff;font-weight:600;display:block}
.foot-base{display:flex;justify-content:space-between;font-size:2.4px;color:#94a3b8;margin-top:16px}
.foot-base span+span{margin-left:6px}

/* misc */
.chips{display:grid;grid-template-columns:1fr 1fr;gap:3px;margin-top:4px}
.chips span{font-size:2.4px;background:#fff;border:.5px solid var(--line);padding:2.5px 1px;text-align:center;border-radius:1px}
.col-title{font-size:3.3px;font-weight:600}
.mini-bars{display:flex;align-items:flex-end;gap:2px;height:12px;margin-top:6px}
.mini-bars i{flex:1;background:linear-gradient(180deg,var(--blue),var(--teal))}
.risk{font-size:2.4px;padding:1.5px 2px;border-radius:1px;margin-top:2px}
.photo{height:46px;border-radius:1px;background:linear-gradient(135deg,#1b2a44,#2c4d7a 60%,#5f7fa3)}
.photo.b{background:linear-gradient(135deg,#dfe3e8,#8d9aaa)}
.photo.c{background:linear-gradient(135deg,#0b2740,#0f5b7a)}
.portrait{width:18px;height:18px;border-radius:50%;margin:0 auto;background:linear-gradient(135deg,#e6d3bf,#9c8472)}
.badge{width:12px;height:12px;border-radius:50%;background:var(--blue);margin:0 auto}
.stat-box b{display:block;font-size:7px;color:var(--blue)}
.stat-box span{font-size:2.4px;color:var(--muted)}
.price{font-size:10px;font-weight:700;margin-top:5px}
.price small{font-size:2.6px;font-weight:400;color:var(--muted)}
.plan{padding:8px 7px}
.plan.hot{border:.8px solid var(--blue);box-shadow:0 3px 8px rgba(37,99,235,.15);position:relative}
.plan.hot .tag{position:absolute;top:-2px;left:50%;transform:translateX(-50%)}
.field{height:5.5px;border:.5px solid var(--line);border-radius:1px;margin-top:3px;font-size:2.2px;color:var(--muted);padding:1.2px 2px}
.field.area{height:15px}
.form-card{padding:8px}
.form-card .btn{margin-top:5px}
</style>
</head>
<body>
<div class="board">

<!-- ============ HOME ============ -->
<section class="page p1">
  <header class="site-head">
    <div class="logo"><i class="logo-dot"></i>PollBeacon</div>
    <nav><span class="on">Home</span><span>Product</span><span>About</span><span>Blog</span><span>Pricing</span><span>Contact</span></nav>
    <span class="lang">◉ EN ▾</span><span class="btn">Request Demo</span>
  </header>
  <div class="hero">
    <div class="hero-photo" role="img" aria-label="Soft, washed-out photo of a team reviewing customer feedback in a bright office"></div>
    <div class="hero-text" style="top:10px">
      <h1>Transform Customer Feedback into <em>Measurable Results</em></h1>
      <p>PollBeacon is a B2B customer experience platform combined with expert consulting services. We collect real-time feedback, segment insights, and help teams act on churn risk before it grows.</p>
      <div class="actions"><span class="btn">Get Started Today</span><span class="btn-o">▸ Watch Demo</span></div>
      <div class="hero-stats"><div><b>500+</b><span>Companies</span></div><div><b>2M+</b><span>Surveys</span></div><div><b>95%</b><span>Satisfaction</span></div></div>
    </div>
    <div class="float" style="left:26px;top:122px"><i class="ico"></i><div><b>35%</b>Avg. Improvement</div></div>
    <div class="dash" style="top:36px">
      <div class="dash-top">CX Analytics Dashboard<span>● Real-time</span></div>
      <div class="dash-sub">Customer Satisfaction Trends<span>Last 30 days</span></div>
      <div class="bars"><i style="height:50%"></i><i style="height:62%"></i><i style="height:72%"></i><i style="height:85%"></i><i style="height:95%"></i></div>
      <div class="dash-stats"><div><b>4.8</b><span>Avg Rating</span></div><div><b>87%</b><span>Satisfaction</span></div><div><b>92%</b><span>Retention</span></div></div>
    </div>
    <div class="float" style="left:335px;top:44px"><i class="ico"></i><div><b>500+</b>Happy Customers</div></div>
    <div class="float" style="left:318px;top:104px"><i class="ico"></i><div><b>24/7</b>Support</div></div>
  </div>
  <div class="sec" style="height:236px">
    <h2 class="sec-title">Platform + Expert Consulting for Complete CX Success</h2>
    <p class="sec-sub">Combining powerful technology with human expertise to drive measurable customer loyalty results</p>
    <div class="grid g3">
      <div class="card"><i class="ico"></i><h4>Real-Time Feedback Collection</h4><p>Capture customer feedback across multiple touchpoints with automated surveys and smart segmentation.</p></div>
      <div class="card"><i class="ico"></i><h4>Leadership-Ready Reporting</h4><p>Transform raw data into executive dashboards with churn-risk alerts and actionable insights.</p></div>
      <div class="card"><i class="ico"></i><h4>Expert CX Consulting</h4><p>Work with our CX specialists who help you implement, interpret, and act on customer insights.</p></div>
      <div class="card"><i class="ico"></i><h4>Churn Risk Alerts</h4><p>Proactive identification of at-risk customers with early warning systems and retention plans.</p></div>
      <div class="card"><i class="ico"></i><h4>Loyalty Measurement</h4><p>Comprehensive loyalty tracking with NPS, CSAT, and custom metrics to measure relationships.</p></div>
      <div class="card"><i class="ico"></i><h4>Seamless Integration</h4><p>Connect with your existing CRM, support tools, and business systems for a unified view.</p></div>
    </div>
  </div>
  <div class="sec soft" style="height:154px">
    <h2 class="sec-title">Trusted by CX Leaders at Medium-to-Large Organizations</h2>
    <p class="sec-sub">See how PollBeacon helps CX leaders, managers and executives drive measurable loyalty results</p>
    <div class="grid g3">
      <div class="card"><p class="quote">"The combination of platform and consulting expertise made all the difference. Our CX team now has clear insights and a plan that improved retention by 35%."</p><div class="person"><i class="avatar" role="img" aria-label="Customer portrait"></i><div><b>Laura Bennett</b><span>VP of Customer Experience, NorthPeak</span></div></div></div>
      <div class="card"><p class="quote">"The churn-risk alerts help us take proactive action before customers leave. Our NPS score increased from 42 to 68 in just 6 months."</p><div class="person"><i class="avatar" role="img" aria-label="Customer portrait"></i><div><b>Kevin Lau</b><span>Head of Customer Success, Global Solutions</span></div></div></div>
      <div class="card"><p class="quote">"Having CX experts who understand both technology and strategy was invaluable. They helped us build a loyalty program that drives results."</p><div class="person"><i class="avatar" role="img" aria-label="Customer portrait"></i><div><b>Nina Ortega</b><span>CX Director, Innovate Labs</span></div></div></div>
    </div>
  </div>
  <div class="cta" style="height:79px">
    <h3>Ready to Drive Measurable Customer Loyalty Results?</h3>
    <p>Join medium-to-large B2B organizations already using PollBeacon's platform and consulting expertise</p>
    <div class="actions"><span class="btn">Request Demo</span><span class="btn-o">Speak with CX Expert</span></div>
  </div>
  <footer class="foot" style="height:88px">
    <div class="foot-row">
      <div class="foot-brand"><div class="logo"><i class="logo-dot"></i>PollBeacon</div><p>B2B customer experience platform combined with expert consulting services to drive measurable loyalty results.</p></div>
      <div class="foot-col"><b>Product</b>Features<br>Pricing<br>Integrations<br>API</div>
      <div class="foot-col"><b>Company</b>About<br>Careers<br>Blog<br>Contact</div>
      <div class="foot-col"><b>Support</b>Help Center<br>Documentation<br>Status<br>Security</div>
    </div>
    <div class="foot-base"><span>© 2024 PollBeacon. All rights reserved.</span><div><span>Privacy Policy</span><span>Terms of Service</span><span>Cookie Policy</span></div></div>
  </footer>
</section>

<!-- ============ PRODUCT ============ -->
<section class="page p2">
  <header class="site-head">
    <div class="logo"><i class="logo-dot"></i>PollBeacon</div>
    <nav><span>Home</span><span class="on">Product</span><span>About</span><span>Blog</span><span>Pricing</span><span>Contact</span></nav>
    <span class="lang">◉ EN ▾</span><span class="btn">Request Demo</span>
  </header>
  <div class="hero">
    <div class="hero-photo" role="img" aria-label="Soft, washed-out photo of analysts working with dashboards"></div>
    <div class="hero-text" style="top:26px">
      <h1>Platform + Expert Consulting for <em>Complete CX Success</em></h1>
      <p>Unlike software-only tools, PollBeacon combines a powerful customer experience platform with expert consulting services. Our CX specialists help you implement, interpret, and act.</p>
      <div class="actions"><span class="btn">Request Demo</span><span class="btn-o">⤓ Download Brochure</span></div>
    </div>
    <div class="dash" style="top:40px">
      <div class="dash-top">Real-Time CX Analytics<span>● Live Data</span></div>
      <div class="dash-sub">Customer Satisfaction Trends<span>Last 30 days</span></div>
      <div class="bars"><i style="height:50%"></i><i style="height:62%"></i><i style="height:72%"></i><i style="height:85%"></i><i style="height:95%"></i></div>
      <div class="dash-stats"><div><b>4.8</b><span>Avg Rating</span></div><div><b>87%</b><span>Satisfaction</span></div><div><b>92%</b><span>Retention</span></div></div>
    </div>
  </div>
  <div class="sec" style="height:241px">
    <h2 class="sec-title">Powerful CX Platform</h2>
    <p class="sec-sub">Advanced technology that captures, analyzes, and reports customer feedback in real-time</p>
    <div class="grid g3">
      <div class="card"><i class="ico"></i><h4>Real-Time Feedback Collection</h4><p>Capture customer feedback across multiple touchpoints with survey design, targeting and smart segmentation.</p></div>
      <div class="card"><i class="ico"></i><h4>Leadership-Ready Reporting</h4><p>Transform raw data into executive dashboards with automated reporting, trend analysis and clear actions.</p></div>
      <div class="card"><i class="ico"></i><h4>Churn Risk Alerts</h4><p>Proactive identification of at-risk customers with early warning systems and recommended retention steps.</p></div>
      <div class="card"><i class="ico"></i><h4>Loyalty Measurement</h4><p>Comprehensive loyalty tracking with NPS, CSAT, CES and custom metrics over time.</p></div>
      <div class="card"><i class="ico"></i><h4>Seamless Integration</h4><p>Connect with your existing CRM, support tools, and marketing platforms for one unified view.</p></div>
      <div class="card"><i class="ico"></i><h4>Enterprise Security</h4><p>Bank-level security with GDPR compliance, SSO integration, encryption and a dedicated manager.</p></div>
    </div>
  </div>
  <div class="sec soft" style="height:310px">
    <h2 class="sec-title">Expert CX Consulting Services</h2>
    <p class="sec-sub">Our certified CX specialists provide strategic guidance and hands-on support to maximize your results</p>
    <div class="grid g3">
      <div class="card"><i class="ico"></i><h4>Implementation &amp; Setup</h4><p>Complete platform setup, survey design, integration configuration, and team training.</p><ul class="ticks"><li>Survey design and optimization</li><li>Integration with existing systems</li><li>Team training and onboarding</li><li>Custom dashboard configuration</li></ul></div>
      <div class="card"><i class="ico"></i><h4>Data Analysis &amp; Insights</h4><p>Expert analysis of your customer feedback data with actionable recommendations.</p><ul class="ticks"><li>Advanced data interpretation</li><li>Trend analysis and benchmarking</li><li>Root cause analysis</li><li>Competitive insights</li></ul></div>
      <div class="card"><i class="ico"></i><h4>Strategy Development</h4><p>Strategic planning and roadmap development to improve customer experience and loyalty.</p><ul class="ticks"><li>CX strategy development</li><li>Customer journey mapping</li><li>Loyalty program design</li><li>ROI measurement frameworks</li></ul></div>
      <div class="card"><i class="ico"></i><h4>Ongoing Support</h4><p>Continuous support and optimization to ensure your CX program evolves and delivers value.</p><ul class="ticks"><li>Monthly strategy reviews</li><li>Performance optimization</li><li>Best practice sharing</li><li>Priority support access</li></ul></div>
    </div>
  </div>
  <div class="sec" style="height:165px">
    <h2 class="sec-title">Advanced Analytics &amp; Data Visualization</h2>
    <p class="sec-sub">See how our platform transforms raw feedback into actionable insights</p>
    <div class="grid g3">
      <div class="card"><div class="col-title">Real-Time Feedback Analysis <span class="tag">Live</span></div><div class="mini-bars"><i style="height:40%"></i><i style="height:60%"></i><i style="height:85%"></i><i style="height:70%"></i></div><p>+23% &nbsp; 4.8</p></div>
      <div class="card"><div class="col-title">Churn Risk Dashboard <span class="tag">Alert</span></div><div class="risk" style="background:#dcfce7">Low Risk: 847</div><div class="risk" style="background:#fef3c7">Medium: 23</div><div class="risk" style="background:#fee2e2">High Risk: 5</div></div>
      <div class="card"><div class="col-title">Customer Journey Map <span class="tag">Interactive</span></div><div style="display:flex;gap:2px;margin-top:5px"><span class="tag">Awareness</span><span class="tag">Consider</span><span class="tag">Purchase</span></div><div class="tag" style="display:block;text-align:center;margin-top:3px">Retention</div></div>
    </div>
  </div>
  <div class="sec" style="height:115px">
    <h2 class="sec-title">Seamless Integration with Your Existing Tools</h2>
    <p class="sec-sub">Connect PollBeacon with your current business systems for a unified customer experience view</p>
    <div class="grid g4">
      <div><div class="col-title">CRM &amp; Sales</div><div class="chips"><span>CloudCRM</span><span>LeadHub</span><span>DealPipe</span><span>BizSuite</span></div></div>
      <div><div class="col-title">Support &amp; Communication</div><div class="chips"><span>DeskFlow</span><span>ChatLine</span><span>TeamTalk</span><span>ChatBridge</span></div></div>
      <div><div class="col-title">Marketing &amp; Analytics</div><div class="chips"><span>WebStats</span><span>MailPilot</span><span>AutoReach</span><span>InsightPro</span></div></div>
      <div><div class="col-title">Business Intelligence</div><div class="chips"><span>VizTable</span><span>DataLens</span><span>QueryView</span><span>ChartLab</span></div></div>
    </div>
  </div>
  <div class="cta" style="height:77px">
    <h3>Ready to Transform Your Customer Experience?</h3>
    <p>See how PollBeacon's platform and consulting expertise can drive measurable results for your organization</p>
    <div class="actions"><span class="btn">Request Demo</span><span class="btn-o">Speak with CX Expert</span></div>
  </div>
  <footer class="foot" style="height:89px">
    <div class="foot-row">
      <div class="foot-brand"><div class="logo"><i class="logo-dot"></i>PollBeacon</div><p>B2B customer experience platform combined with expert consulting services to drive measurable loyalty results.</p></div>
      <div class="foot-col"><b>Product</b>Features<br>Pricing<br>Integrations<br>API</div>
      <div class="foot-col"><b>Company</b>About<br>Careers<br>Blog<br>Contact</div>
      <div class="foot-col"><b>Support</b>Help Center<br>Documentation<br>Status<br>Security</div>
    </div>
    <div class="foot-base"><span>© 2024 PollBeacon. All rights reserved.</span><div><span>Privacy Policy</span><span>Terms of Service</span><span>Cookie Policy</span></div></div>
  </footer>
</section>

<!-- ============ ABOUT ============ -->
<section class="page p3">
  <header class="site-head">
    <div class="logo"><i class="logo-dot"></i>PollBeacon</div>
    <nav><span>Home</span><span>Product</span><span class="on">About</span><span>Blog</span><span>Pricing</span><span>Contact</span></nav>
    <span class="lang">◉ EN ▾</span><span class="btn">Request Demo</span>
  </header>
  <div class="hero">
    <div class="hero-photo" role="img" aria-label="Soft, washed-out photo of the consulting team in a meeting room"></div>
    <div class="hero-text" style="top:42px;width:135px">
      <h1>Building Trust Through <em>Expertise &amp; Innovation</em></h1>
      <p>PollBeacon was founded on the belief that customer experience transformation requires both powerful technology and human expertise. We combine advanced analytics with certified CX specialists to deliver results.</p>
    </div>
  </div>
  <div class="sec" style="height:131px">
    <div class="grid g3" style="margin-top:20px">
      <div class="card center"><i class="ico round"></i><h4>Our Mission</h4><p>To empower B2B organizations with the technology and expertise needed to turn customer feedback into actionable insights that drive loyalty and growth.</p></div>
      <div class="card center"><i class="ico round"></i><h4>Our Vision</h4><p>To become the leading platform for customer experience transformation, where every organization can measure and improve relationships.</p></div>
      <div class="card center"><i class="ico round"></i><h4>Our Values</h4><p>Trust, innovation, and results-driven approach. We believe in combining cutting-edge technology with human expertise.</p></div>
    </div>
  </div>
  <div class="sec soft" style="height:160px;text-align:left">
    <h2 class="sec-title">Our Story</h2>
    <div style="display:flex;gap:14px;margin-top:8px">
      <div style="width:170px">
        <p class="card" style="border:0;box-shadow:none;background:none;padding:0"><span style="font-size:2.8px;color:var(--muted);line-height:1.55;display:block">Founded by a team of customer experience veterans and technology innovators, PollBeacon emerged from a simple observation: most organizations struggle to turn customer feedback into meaningful action.<br><br>While working with large enterprises, our founders noticed that despite having access to customer data, many organizations lacked the expertise to interpret insights and implement effective strategies. This gap inspired the creation of PollBeacon.<br><br>Today, we combine advanced analytics technology with certified CX consulting to help medium-to-large B2B organizations not just collect feedback, but transform it into measurable business results and lasting loyalty.</span></p>
      </div>
      <div style="display:grid;grid-template-columns:1fr 1fr;gap:14px 10px;text-align:center;flex:1">
        <div class="stat-box"><b>500+</b><span>Companies Served</span></div>
        <div class="stat-box"><b>2M+</b><span>Surveys Collected</span></div>
        <div class="stat-box"><b>95%</b><span>Client Satisfaction</span></div>
        <div class="stat-box"><b>35%</b><span>Avg. Retention Improvement</span></div>
      </div>
    </div>
  </div>
  <div class="sec" style="height:195px">
    <h2 class="sec-title">Meet Our CX Experts</h2>
    <p class="sec-sub">Our team combines deep customer experience expertise with cutting-edge technology innovation</p>
    <div class="grid g4">
      <div class="card center"><div class="portrait" role="img" aria-label="Portrait of Laura Bennett"></div><h4>Laura Bennett</h4><p class="link">CEO &amp; Co-Founder</p><p>15+ years in customer experience leadership at global firms, certified CX professional.</p></div>
      <div class="card center"><div class="portrait" role="img" aria-label="Portrait of Kevin Lau"></div><h4>Kevin Lau</h4><p class="link">CTO &amp; Co-Founder</p><p>Technology leader with expertise in data analytics and feedback platforms.</p></div>
      <div class="card center"><div class="portrait" role="img" aria-label="Portrait of Nina Ortega"></div><h4>Nina Ortega</h4><p class="link">Head of CX Consulting</p><p>Certified CX professional who has helped 200+ companies improve retention.</p></div>
      <div class="card center"><div class="portrait" role="img" aria-label="Portrait of Daniel Park"></div><h4>Daniel Park</h4><p class="link">VP of Customer Success</p><p>Customer success expert with deep experience in B2B SaaS and loyalty.</p></div>
    </div>
  </div>
  <div class="sec" style="height:118px">
    <h2 class="sec-title">Trusted &amp; Recognized</h2>
    <p class="sec-sub">Our expertise is backed by industry certifications and recognition</p>
    <div class="grid g4">
      <div class="card center"><div class="badge"></div><h4>CX Certified</h4><p>Certified Customer Experience Professional</p></div>
      <div class="card center"><div class="badge"></div><h4>ISO 27001</h4><p>Information Security Management</p></div>
      <div class="card center"><div class="badge"></div><h4>GDPR Compliant</h4><p>Data Protection &amp; Privacy</p></div>
      <div class="card center"><div class="badge"></div><h4>CX Excellence Award</h4><p>Best CX Platform 2024</p></div>
    </div>
  </div>
  <div class="cta" style="height:79px">
    <h3>Ready to Work with CX Experts?</h3>
    <p>Join 500+ organizations already benefiting from our platform and consulting expertise</p>
    <div class="actions"><span class="btn">Request Demo</span><span class="btn-o">Meet Our Team</span></div>
  </div>
  <footer class="foot" style="height:88px">
    <div class="foot-row">
      <div class="foot-brand"><div class="logo"><i class="logo-dot"></i>PollBeacon</div><p>B2B customer experience platform combined with expert consulting services to drive measurable loyalty results.</p></div>
      <div class="foot-col"><b>Product</b>Features<br>Pricing<br>Integrations<br>API</div>
      <div class="foot-col"><b>Company</b>About<br>Careers<br>Blog<br>Contact</div>
      <div class="foot-col"><b>Support</b>Help Center<br>Documentation<br>Status<br>Security</div>
    </div>
    <div class="foot-base"><span>© 2024 PollBeacon. All rights reserved.</span><div><span>Privacy Policy</span><span>Terms of Service</span><span>Cookie Policy</span></div></div>
  </footer>
</section>

<!-- ============ BLOG ============ -->
<section class="page p4">
  <header class="site-head">
    <div class="logo"><i class="logo-dot"></i>PollBeacon</div>
    <nav><span>Home</span><span>Product</span><span>About</span><span class="on">Blog</span><span>Pricing</span><span>Contact</span></nav>
    <span class="lang">◉ EN ▾</span><span class="btn">Request Demo</span>
  </header>
  <div class="hero">
    <div class="hero-photo" role="img" aria-label="Soft, washed-out photo of a desk with reports and a laptop"></div>
    <div class="hero-text" style="top:48px;width:135px">
      <h1>Customer Experience <em>Insights &amp; Resources</em></h1>
      <p>Stay ahead with the latest insights, best practices, and strategies for transforming customer experience programs in B2B organizations.</p>
    </div>
  </div>
  <div class="sec" style="height:115px;text-align:left">
    <div style="display:flex;gap:10px;margin-top:20px;align-items:center">
      <div style="flex:1"><span class="tag">Featured Article</span><h2 style="font-size:6.5px;font-weight:600;margin-top:3px;line-height:1.2">The Complete Guide to B2B Customer Experience Transformation</h2><p style="font-size:2.8px;color:var(--muted);line-height:1.5;margin-top:3px">Learn how medium-to-large organizations are successfully transforming their customer experience programs with the right combination of technology and expert guidance.</p><p class="meta">By Laura Bennett, CEO &nbsp; December 15, 2024 &nbsp; 8 min read</p><span class="btn" style="margin-top:4px">Read Full Article</span></div>
      <div class="photo" style="width:84px;height:57px" role="img" aria-label="Team meeting around a boardroom table with a presentation screen"></div>
    </div>
  </div>
  <div class="sec soft" style="height:145px">
    <h2 class="sec-title">Browse by Category</h2>
    <p class="sec-sub">Find content tailored to your specific needs</p>
    <div class="grid g4">
      <div class="card center"><i class="ico"></i><h4>Analytics &amp; Insights</h4><p>Data-driven strategies for understanding customer behavior and preferences</p><p class="link">12 articles</p></div>
      <div class="card center"><i class="ico"></i><h4>Customer Success</h4><p>Best practices for improving customer satisfaction and retention</p><p class="link">18 articles</p></div>
      <div class="card center"><i class="ico"></i><h4>Implementation</h4><p>Step-by-step guides for setting up and optimizing CX programs</p><p class="link">15 articles</p></div>
      <div class="card center"><i class="ico"></i><h4>Strategy &amp; Planning</h4><p>Strategic insights for building effective customer experience programs</p><p class="link">10 articles</p></div>
    </div>
  </div>
  <div class="sec" style="height:395px">
    <h2 class="sec-title">Latest Articles</h2>
    <p class="sec-sub">Stay updated with the latest trends and insights</p>
    <div class="grid g3">
      <div class="card" style="padding:0"><div class="photo c" role="img" aria-label="Laptop showing analytics charts"></div><div style="padding:5px"><span class="tag">Analytics</span><h4>5 Key Metrics Every B2B Organization Should Track</h4><p>Discover the essential customer experience metrics that drive business growth and loyalty in B2B environments.</p><p class="meta">Kevin Lau · Dec 12, 2024 · 6 min read</p></div></div>
      <div class="card" style="padding:0"><div class="photo b" role="img" aria-label="Colleagues discussing around a table"></div><div style="padding:5px"><span class="tag">Customer Success</span><h4>Building a Customer-Centric Culture in Large Organizations</h4><p>Learn how to transform your organization's culture to prioritize customer experience at every level.</p><p class="meta">Nina Ortega · Dec 10, 2024 · 7 min read</p></div></div>
      <div class="card" style="padding:0"><div class="photo" role="img" aria-label="Dashboard screen with red and green charts"></div><div style="padding:5px"><span class="tag">Strategy</span><h4>Reducing Churn Risk with Proactive Customer Insights</h4><p>Implement early warning systems and proactive strategies to identify and retain at-risk customers.</p><p class="meta">Daniel Park · Dec 8, 2024 · 8 min read</p></div></div>
      <div class="card" style="padding:0"><div class="photo b" role="img" aria-label="Hands writing notes next to a laptop"></div><div style="padding:5px"><span class="tag">Implementation</span><h4>Getting Started with Customer Feedback Programs</h4><p>A comprehensive guide to launching your first customer experience program successfully.</p><p class="meta">Laura Bennett · Dec 5, 2024 · 10 min read</p></div></div>
      <div class="card" style="padding:0"><div class="photo c" role="img" aria-label="Abstract blue circuit board"></div><div style="padding:5px"><span class="tag">Analytics</span><h4>AI-Powered Customer Insights: What's Next?</h4><p>Explore how artificial intelligence is revolutionizing customer experience analytics and prediction.</p><p class="meta">Kevin Lau · Dec 3, 2024 · 9 min read</p></div></div>
      <div class="card" style="padding:0"><div class="photo c" role="img" aria-label="Rising green growth chart on screen"></div><div style="padding:5px"><span class="tag">Customer Success</span><h4>Case Study: How NorthPeak Improved NPS by 40%</h4><p>An in-depth look at how one organization transformed their customer experience program.</p><p class="meta">Nina Ortega · Nov 30, 2024 · 12 min read</p></div></div>
    </div>
  </div>
  <div class="sec" style="height:155px">
    <h2 class="sec-title">Free Resources</h2>
    <p class="sec-sub">Download our latest guides, templates, and tools</p>
    <div class="grid g4">
      <div class="card center"><i class="ico"></i><h4>CX Strategy Template</h4><p>Comprehensive template for building your customer experience strategy</p><span class="btn-o" style="margin-top:4px">Download PDF</span></div>
      <div class="card center"><i class="ico"></i><h4>Survey Design Guide</h4><p>Best practices for creating effective customer feedback surveys</p><span class="btn-o" style="margin-top:4px">Download Guide</span></div>
      <div class="card center"><i class="ico"></i><h4>ROI Calculator</h4><p>Calculate the potential return on investment for your CX program</p><span class="btn-o" style="margin-top:4px">Use Calculator</span></div>
      <div class="card center"><i class="ico"></i><h4>Implementation Checklist</h4><p>Step-by-step checklist for launching your customer experience program</p><span class="btn-o" style="margin-top:4px">Download Checklist</span></div>
    </div>
  </div>
  <div class="cta" style="height:91px">
    <h3>Stay Updated</h3>
    <p>Get the latest CX insights, best practices, and industry trends delivered to your inbox</p>
    <div class="subscribe"><i>Enter your email address</i><span class="btn">Subscribe</span></div>
    <p style="font-size:2.4px;margin-top:3px">No spam, unsubscribe at any time. We respect your privacy.</p>
  </div>
  <footer class="foot" style="height:88px">
    <div class="foot-row">
      <div class="foot-brand"><div class="logo"><i class="logo-dot"></i>PollBeacon</div><p>B2B customer experience platform combined with expert consulting services to drive measurable loyalty results.</p></div>
      <div class="foot-col"><b>Product</b>Features<br>Pricing<br>Integrations<br>API</div>
      <div class="foot-col"><b>Company</b>About<br>Careers<br>Blog<br>Contact</div>
      <div class="foot-col"><b>Support</b>Help Center<br>Documentation<br>Status<br>Security</div>
    </div>
    <div class="foot-base"><span>© 2024 PollBeacon. All rights reserved.</span><div><span>Privacy Policy</span><span>Terms of Service</span><span>Cookie Policy</span></div></div>
  </footer>
</section>

<!-- ============ PRICING ============ -->
<section class="page p5">
  <header class="site-head">
    <div class="logo"><i class="logo-dot"></i>PollBeacon</div>
    <nav><span>Home</span><span>Product</span><span>About</span><span>Blog</span><span class="on">Pricing</span><span>Contact</span></nav>
    <span class="lang">◉ EN ▾</span><span class="btn">Request Demo</span>
  </header>
  <div class="hero">
    <div class="hero-photo" role="img" aria-label="Soft, washed-out photo of people reviewing documents at a desk"></div>
    <div class="hero-text" style="top:45px;width:140px">
      <h1>Transparent Pricing for <em>Measurable Results</em></h1>
      <p>Choose the plan that fits your organization's needs. All plans include our powerful platform and expert consulting services to ensure your success.</p>
      <div class="toggle"><span>Monthly</span><i></i><span>Annual <em>(Save 20%)</em></span></div>
    </div>
  </div>
  <div class="sec" style="height:236px">
    <div class="grid g3" style="margin-top:30px;align-items:start">
      <div class="card plan center"><h4>Starter</h4><p>Perfect for growing teams starting their CX journey</p><div class="price">$2,500<small>/month</small></div><ul class="ticks" style="text-align:left"><li>Up to 1,000 surveys/month</li><li>Basic analytics dashboard</li><li>Email &amp; web surveys</li><li>Standard integrations</li><li>Email support</li><li>4 hours consulting/month</li><li>Basic reporting</li></ul></div>
      <div class="card plan hot center"><span class="tag">Most Popular</span><h4>Professional</h4><p>Ideal for medium-sized organizations with established CX programs</p><div class="price">$5,000<small>/month</small></div><ul class="ticks" style="text-align:left"><li>Everything in Starter, plus:</li><li>Up to 5,000 surveys/month</li><li>Advanced analytics &amp; AI insights</li><li>Multi-channel feedback collection</li><li>Advanced integrations</li><li>Priority support</li><li>8 hours consulting/month</li><li>Custom dashboards</li><li>Churn risk alerts</li><li>API access</li></ul><span class="btn" style="margin-top:5px">Get Started</span></div>
      <div class="card plan center"><h4>Enterprise</h4><p>For large organizations with complex CX needs</p><div class="price">$10,000<small>/month</small></div><ul class="ticks" style="text-align:left"><li>Everything in Professional, plus:</li><li>Unlimited surveys</li><li>White-label options</li><li>Custom integrations</li><li>Dedicated success manager</li><li>24/7 phone support</li><li>16 hours consulting/month</li><li>Advanced security features</li><li>Custom reporting</li><li>Multi-language support</li></ul></div>
    </div>
  </div>
  <div class="sec soft" style="height:195px">
    <h2 class="sec-title">Additional Consulting Services</h2>
    <p class="sec-sub">Supplement your plan with additional expert consulting hours</p>
    <div class="grid g3">
      <div class="card center"><i class="ico"></i><h4>Implementation Package</h4><div class="price" style="font-size:6px;color:var(--blue)">$5,000</div><p>Complete platform setup and team training</p><ul class="ticks" style="text-align:left"><li>Survey design &amp; optimization</li><li>Integration configuration</li><li>Team training sessions</li><li>Custom dashboard setup</li><li>30-day success guarantee</li></ul></div>
      <div class="card center"><i class="ico"></i><h4>Strategy Development</h4><div class="price" style="font-size:6px;color:var(--blue)">$3,000</div><p>Comprehensive CX strategy and roadmap</p><ul class="ticks" style="text-align:left"><li>Customer journey mapping</li><li>CX strategy development</li><li>Loyalty program design</li><li>ROI measurement framework</li><li>Implementation roadmap</li></ul></div>
      <div class="card center"><i class="ico"></i><h4>Additional Hours</h4><div class="price" style="font-size:6px;color:var(--blue)">$200/hour</div><p>Flexible consulting hours for ongoing support</p><ul class="ticks" style="text-align:left"><li>Data analysis &amp; insights</li><li>Strategy refinement</li><li>Team coaching</li><li>Best practice guidance</li><li>Priority support access</li></ul></div>
    </div>
  </div>
  <div class="sec" style="height:230px">
    <h2 class="sec-title">Frequently Asked Questions</h2>
    <p class="sec-sub">Everything you need to know about our pricing and services</p>
    <div class="grid g3">
      <div class="card"><h4 style="margin-top:0">What's included in the consulting hours?</h4><p>Our consulting hours include strategic guidance, data analysis, implementation support, team training, and ongoing optimization with a dedicated CX expert.</p></div>
      <div class="card"><h4 style="margin-top:0">Can I upgrade or downgrade my plan?</h4><p>Yes, you can change your plan at any time. Upgrades take effect immediately, and downgrades take effect at the next billing cycle.</p></div>
      <div class="card"><h4 style="margin-top:0">Do you offer custom pricing for large organizations?</h4><p>Absolutely. For organizations with unique needs or very high volumes, we offer custom enterprise solutions with tailored pricing.</p></div>
      <div class="card"><h4 style="margin-top:0">What's your refund policy?</h4><p>We offer a 30-day money-back guarantee. If you're not satisfied within the first 30 days, we'll provide a full refund.</p></div>
      <div class="card"><h4 style="margin-top:0">Are there any setup fees?</h4><p>No setup fees for any of our standard plans. The Implementation Package is optional and provides additional hands-on setup.</p></div>
      <div class="card"><h4 style="margin-top:0">Do you offer multi-year discounts?</h4><p>Yes, we offer significant discounts for annual billing (20% off) and multi-year commitments. Contact our sales team.</p></div>
    </div>
  </div>
  <div class="cta" style="height:66px">
    <h3 style="padding-top:16px">Ready to Get Started?</h3>
    <p>Choose the plan that fits your organization or speak with our experts for a custom solution</p>
    <div class="actions"><span class="btn">Start Free Trial</span><span class="btn-o">Contact Sales</span></div>
  </div>
  <footer class="foot" style="height:101px">
    <div class="foot-row">
      <div class="foot-brand"><div class="logo"><i class="logo-dot"></i>PollBeacon</div><p>B2B customer experience platform combined with expert consulting services to drive measurable loyalty results.</p></div>
      <div class="foot-col"><b>Product</b>Features<br>Pricing<br>Integrations<br>API</div>
      <div class="foot-col"><b>Company</b>About<br>Careers<br>Blog<br>Contact</div>
      <div class="foot-col"><b>Support</b>Help Center<br>Documentation<br>Status<br>Security</div>
    </div>
    <div class="foot-base"><span>© 2024 PollBeacon. All rights reserved.</span><div><span>Privacy Policy</span><span>Terms of Service</span><span>Cookie Policy</span></div></div>
  </footer>
</section>

<!-- ============ CONTACT ============ -->
<section class="page p6">
  <header class="site-head">
    <div class="logo"><i class="logo-dot"></i>PollBeacon</div>
    <nav><span>Home</span><span>Product</span><span>About</span><span>Blog</span><span>Pricing</span><span class="on">Contact</span></nav>
    <span class="lang">◉ EN ▾</span><span class="btn">Request Demo</span>
  </header>
  <div class="hero">
    <div class="hero-photo" role="img" aria-label="Soft, washed-out photo of a support specialist wearing a headset"></div>
    <div class="hero-text" style="top:54px;width:140px">
      <h1>Get in Touch with Our <em>CX Experts</em></h1>
      <p>Ready to transform your customer experience? Our team of CX specialists is here to help you implement, optimize, and scale your customer feedback programs.</p>
    </div>
  </div>
  <div class="sec soft" style="height:380px;text-align:left">
    <div class="grid g2" style="margin-top:20px;align-items:start">
      <div class="card form-card"><i class="ico"></i><h4>Request a Demo</h4><p>See PollBeacon in action with a personalized demonstration tailored to your organization's needs.</p>
        <div class="field" style="margin-top:6px">Full Name</div><div class="field">Work Email</div><div class="field">Company Name</div><div class="field">Company Size ▾</div><div class="field">Your Role ▾</div><div class="field area">Tell us about your CX challenges and goals</div><span class="btn">Schedule Demo</span></div>
      <div class="card form-card"><i class="ico"></i><h4>Speak with a CX Expert</h4><p>Get personalized guidance from our certified customer experience specialists.</p>
        <div class="field" style="margin-top:6px">Full Name</div><div class="field">Work Email</div><div class="field">Company Name</div><div class="field">Phone Number</div><div class="field">Consulting Focus ▾</div><div class="field area">Describe your specific needs and timeline</div><span class="btn">Connect with Expert</span></div>
      <div class="card form-card"><i class="ico"></i><h4>General Inquiry</h4><p>Have questions about our platform, pricing, or services? We're here to help.</p>
        <div class="field" style="margin-top:6px">Full Name</div><div class="field">Work Email</div><div class="field">Company Name</div><div class="field">Inquiry Type ▾</div><div class="field area">How can we help you?</div><span class="btn">Send Message</span></div>
    </div>
  </div>
  <div class="sec soft" style="height:120px">
    <h2 class="sec-title">Get in Touch</h2>
    <p class="sec-sub">Multiple ways to reach our team</p>
    <div class="grid g4">
      <div class="card center"><i class="ico"></i><h4>Phone</h4><p>+1 (555) 010-2040<br>Mon–Fri, 9AM–6PM EST</p></div>
      <div class="card center"><i class="ico"></i><h4>Email</h4><p>hello@pollbeacon.example<br>We respond within 24 hours</p></div>
      <div class="card center"><i class="ico"></i><h4>Office</h4><p>48 Harbor Lane<br>Suite 210, Boston</p></div>
      <div class="card center"><i class="ico"></i><h4>Live Chat</h4><p>Available on our website<br>Mon–Fri, 9AM–6PM EST</p></div>
    </div>
  </div>
  <div class="sec" style="height:226px">
    <h2 class="sec-title">Quick Answers</h2>
    <p class="sec-sub">Find answers to common questions</p>
    <div class="grid g3">
      <div class="card"><h4 style="margin-top:0">How quickly can I get started?</h4><p>Most organizations can be up and running within 2–3 weeks, including platform setup, integrations, and initial survey deployment.</p></div>
      <div class="card"><h4 style="margin-top:0">Do you offer training for our team?</h4><p>Yes, all plans include training sessions. We provide comprehensive training on platform usage, survey design, and data interpretation.</p></div>
      <div class="card"><h4 style="margin-top:0">What kind of support do you provide?</h4><p>We offer email, phone, and live chat support depending on your plan. Enterprise customers get dedicated success management.</p></div>
      <div class="card"><h4 style="margin-top:0">Can I integrate with my existing tools?</h4><p>Absolutely. We integrate with 50+ popular business tools including CRM, support, marketing, and analytics platforms.</p></div>
    </div>
  </div>
  <footer class="foot" style="height:88px">
    <div class="foot-row">
      <div class="foot-brand"><div class="logo"><i class="logo-dot"></i>PollBeacon</div><p>B2B customer experience platform combined with expert consulting services to drive measurable loyalty results.</p></div>
      <div class="foot-col"><b>Product</b>Features<br>Pricing<br>Integrations<br>API</div>
      <div class="foot-col"><b>Company</b>About<br>Careers<br>Blog<br>Contact</div>
      <div class="foot-col"><b>Support</b>Help Center<br>Documentation<br>Status<br>Security</div>
    </div>
    <div class="foot-base"><span>© 2024 PollBeacon. All rights reserved.</span><div><span>Privacy Policy</span><span>Terms of Service</span><span>Cookie Policy</span></div></div>
  </footer>
</section>

</div>
</body>
</html>
```